A Maple Syrup Label for a Local Buniness

We are looking for a label for our maple syrup business. Our business currently sells honey, and we are expanding into maple syrup. Our Business name is "Brackley Honey" and we currently have a logo attached below. We would like to incorporate the bee and BH part, but the label could also read "Brackley Farms" with the words maple syrup. We do not want consumers to confuse the maple syrup jars with the honey jars. It should be clear that the jars contain maple syrup. We are open to new designs as well.

```html
<!DOCTYPE html>
<html lang="en">
<head>
<meta charset="utf-8">
<title>Brackley Farms – Maple Syrup Label</title>
<link href="https://fonts.googleapis.com/css2?family=Cinzel:wght@600&family=Tinos&family=Arimo&display=swap" rel="stylesheet">
<style>
  :root {
    --backdrop: #eeeeee;
    --label-black: #1e1f1f;
    --ink-white: #f4f4f2;
    --maple-amber: #f0a22a;
  }
  html, body {
    margin: 0;
    padding: 0;
    width: 1200px;
    height: 1200px;
    overflow: hidden;
    background: var(--backdrop);
  }
  .canvas {
    position: relative;
    width: 1200px;
    height: 1200px;
  }
  .label-shape {
    position: absolute;
    inset: 0;
  }
  .label-shape path { fill: var(--label-black); }
  .brand-mark {
    position: absolute;
    left: 455px;
    top: 200px;
    width: 290px;
    height: 290px;
    box-sizing: border-box;
    border: 6px solid var(--maple-amber);
    border-radius: 50%;
  }
  .brand-name {
    position: absolute;
    left: 250px;
    width: 700px;
    top: 500px;
    margin: 0;
    text-align: center;
    font-family: "Cinzel", "Times New Roman", serif;
    font-weight: 600;
    font-size: 92px;
    line-height: 112px;
    letter-spacing: 1px;
    color: var(--ink-white);
  }
  .net-weight {
    position: absolute;
    left: 250px;
    width: 700px;
    top: 818px;
    margin: 0;
    text-align: center;
    font-family: "Arimo", Arial, sans-serif;
    font-size: 40px;
    color: var(--ink-white);
  }
  .product-name {
    position: absolute;
    left: 250px;
    width: 700px;
    top: 928px;
    margin: 0;
    text-align: center;
    font-family: "Tinos", "Times New Roman", serif;
    font-size: 64px;
    letter-spacing: 1px;
    color: var(--ink-white);
  }
</style>
</head>
<body>
<main class="canvas">
  <svg class="label-shape" width="1200" height="1200" viewBox="0 0 1200 1200" aria-hidden="true">
    <path d="M250 382 Q250 362 270 362 L340 362 Q357 362 357 345 L357 330 C357 190 470 100 600 100 C730 100 843 190 843 330 L843 345 Q843 362 860 362 L930 362 Q950 362 950 382 L950 1080 Q950 1100 930 1100 L270 1100 Q250 1100 250 1080 Z"/>
  </svg>
  <div class="brand-mark" aria-hidden="true"></div>
  <h1 class="brand-name">BRACKLEY<br>FARMS</h1>
  <p class="net-weight">500g</p>
  <p class="product-name">MAPLE SYRUP</p>
</main>
</body>
</html>
```